Torvel Cleaning Company Flyer

Hi, We need an A4 flyer design for our cleaning company, focusing on dry carpet cleaning I attached our catalogue to give some idea. In addition, our websites can provide more information. Our Services:-General Cleaning Carry out heavy cleansing tasks and special projects. Clean, stock and supply designated facility areas (dusting, sweeping, vacuuming, mopping, cleaning ceiling vents, restroom cleaning etc).Using electrically powered scrubbing and polishing machines to burnish, scrub, polish and spray clean floors. Window Cleaning Regular, Reliable Window Cleaning.Hard To Reach Windows.Single 7 Multi-Storey.Frames and Glass Cleaned.Floor Cleaning Cleaning Marble Cleaning & Polishing.Tile & Grout Cleaning.Hardwood Floors Services.Vinyl Floors.The MIRA Dry Extraction Carpet Cleaning System uses environmentally preferred, Blue Fern Certified cleaning products that deep cleans your carpets and textured hard floors quickly and easily.

Target Market(s)

Commercial Cleaning residential Cleaning Hotel cleaning

Industry/Entity Type

Cleaning Service

Contact Information for Business Card

Samir Tareq Al-Hudhaili Gm
Derek Plume Marketing Manger

Font styles to use
Serif
Sans Serif

Colors
0355a3
3176b5
85acd3
cee9f5
85cae6
34a6d7
0592cd

```html
<!DOCTYPE html>
<html lang="en">
<head>
<meta charset="utf-8">
<title>Torvel Cleaning – Dry Carpet Cleaning Flyer</title>
<link href="https://fonts.googleapis.com/css2?family=Montserrat:wght@300;400;500;600;700&display=swap" rel="stylesheet">
<style>
  :root{
    --navy:#2b3190;
    --royal:#0355a3;
    --steel:#3176b5;
    --sky:#34a6d7;
    --bright:#40c0ef;
    --cyan:#0592cd;
    --pale:#cee9f5;
    --mist:#85acd3;
    --charcoal:#3b3b3d;
    --ink:#2e2e33;
    --stage:#e4e5e7;
  }
  *{box-sizing:border-box;margin:0;padding:0}
  html,body{width:1200px;height:986px;overflow:hidden;background:var(--stage);font-family:"Montserrat",Arial,sans-serif;color:var(--ink)}
  .flyer{position:absolute;left:268px;top:23px;width:664px;height:940px;background:#fff;overflow:hidden;box-shadow:0 6px 24px rgba(0,0,0,.12)}
  .hero-photo{position:absolute;left:0;top:0;width:664px;height:370px;background:linear-gradient(135deg,#d9d4cf 0%,#ece9e6 40%,#b9c2cc 75%,#5b78a8 100%)}
  .waves{position:absolute;left:0;top:0}
  .brand{position:absolute;left:30px;top:36px;font-weight:700;font-size:26px;color:var(--royal);letter-spacing:.5px;display:flex;align-items:center;gap:8px}
  .brand-dot{width:14px;height:14px;border-radius:50%;background:var(--bright)}
  .headline{position:absolute;left:34px;top:160px}
  .headline .kicker{display:block;font-weight:700;font-size:34px;color:var(--bright);letter-spacing:1px}
  .headline .main{display:block;font-weight:300;font-size:66px;line-height:1;color:var(--navy);letter-spacing:-1px}
  .job-photo{position:absolute;left:482px;top:222px;width:156px;height:156px;border-radius:50%;border:4px solid #fff;background:linear-gradient(160deg,#9a6a4c 0%,#c8a07e 45%,#e8e4df 100%)}
  .services{position:absolute;left:32px;top:412px;width:330px}
  .section-title{font-weight:700;font-size:17px;color:var(--bright);letter-spacing:.5px;margin-bottom:6px}
  .intro{font-size:11.5px;line-height:1.35;margin-bottom:14px}
  .lists{display:flex;gap:18px}
  .ticks{list-style:none;font-size:12px;line-height:1.25}
  .ticks li{position:relative;padding-left:24px;margin-bottom:7px}
  .ticks li::before{content:"";position:absolute;left:0;top:2px;width:11px;height:11px;border-radius:50%;background:var(--navy)}
  .ticks li::after{content:"";position:absolute;left:3.5px;top:4px;width:3px;height:5px;border:solid #fff;border-width:0 1.5px 1.5px 0;transform:rotate(45deg)}
  .machines-note{position:absolute;left:386px;top:402px;width:250px;font-size:11.5px;line-height:1.35;text-align:justify}
  .equipment{position:absolute;left:392px;top:462px;width:246px;height:150px;border:1px solid var(--navy);border-radius:16px;background:#fff}
  .equipment .shot{position:absolute;left:40px;top:22px;width:166px;height:106px;border-radius:6px;background:linear-gradient(180deg,#3e4a78 0%,#7d86a0 60%,#c9ccd2 100%)}
  .system-note{position:absolute;left:392px;top:626px;width:246px;font-size:11px;line-height:1.35;text-align:justify}
  .system-mark{position:absolute;left:520px;top:700px;font-weight:700;font-size:30px;color:var(--navy);letter-spacing:-1px}
  .windows{position:absolute;left:0;top:722px;width:420px;height:84px;background:var(--pale);border-radius:0 24px 24px 0;padding:14px 20px 0 34px}
  .windows h3{font-weight:700;font-size:15px;color:var(--navy);margin-bottom:4px}
  .windows p{font-size:12px;line-height:1.35}
  .call{position:absolute;left:34px;top:816px;font-weight:700;font-size:26px;color:var(--ink)}
  .call .number{font-weight:400;font-size:32px;color:var(--navy);margin-left:14px}
  .footer-band{position:absolute;left:0;top:830px}
  .contact{position:absolute;left:0;top:900px;width:664px;display:flex;justify-content:space-between;padding:0 28px;font-size:12px;font-weight:600;color:#fff}
  .contact span{display:flex;align-items:center;gap:7px}
</style>
</head>
<body>
<article class="flyer">
  <div class="hero-photo" role="img" aria-label="Photo of a cleaner in a blue shirt bent over a beige sofa in a bright living room"></div>

  <svg class="waves" width="664" height="420" viewBox="0 0 664 420" aria-hidden="true">
    <path d="M0 330 C160 350 300 320 420 270 C520 228 600 215 664 218 L664 420 L0 420 Z" fill="var(--bright)"/>
    <path d="M0 352 C180 372 320 345 440 300 C540 262 610 250 664 255 L664 420 L0 420 Z" fill="var(--navy)"/>
    <path d="M0 372 C200 388 340 370 460 330 C560 296 620 286 664 288 L664 420 L0 420 Z" fill="#fff"/>
  </svg>

  <div class="brand"><span class="brand-dot"></span>Torvel Cleaning</div>

  <h1 class="headline">
    <span class="kicker">DRY CARPET</span>
    <span class="main">CLEANING</span>
  </h1>

  <div class="job-photo" role="img" aria-label="Photo of a worker operating a floor polishing machine on a marble floor"></div>

  <section class="services">
    <h2 class="section-title">OUR SERVICES:</h2>
    <p class="intro">General Cleaning Carry out heavy cleansing tasks and special projects. Clean, stock and supply designated facility areas</p>
    <div class="lists">
      <ul class="ticks">
        <li>Dusting</li>
        <li>Sweeping</li>
        <li>Vacuuming</li>
        <li>Marble Cleaning<br>&amp; Polishing</li>
        <li>Floor Cleaning</li>
        <li>Tile &amp; Grout Cleaning.</li>
      </ul>
      <ul class="ticks">
        <li>Mopping</li>
        <li>Cleaning ceiling vents</li>
        <li>Restroom cleaning</li>
        <li>Hardwood Floors<br>Services.</li>
        <li>Vinyl Floors.</li>
      </ul>
    </div>
  </section>

  <p class="machines-note">Using electrically powered scrubbing and polishing machines to burnish, scrub, polish and spray clean floors.</p>

  <div class="equipment">
    <div class="shot" role="img" aria-label="Product photo of dry extraction carpet cleaning machines and cleaning product tubs"></div>
  </div>

  <p class="system-note">The MIRA Dry Extraction Carpet Cleaning System uses environmentally preferred, Blue Fern Certified cleaning products that deep cleans your carpets and textured hard floors quickly and easily.</p>

  <div class="system-mark">MIRA</div>

  <section class="windows">
    <h3>HARD TO REACH WINDOWS!</h3>
    <p>Window Cleaning Regular, Reliable Window Cleaning.<br>Single 7 Multi-Storey.Frames and Glass Cleaned.</p>
  </section>

  <p class="call">Call us on <span class="number">4410 5583</span></p>

  <svg class="footer-band" width="664" height="110" viewBox="0 0 664 110" aria-hidden="true">
    <path d="M0 60 C220 62 440 40 664 0 L664 110 L0 110 Z" fill="var(--bright)"/>
    <path d="M0 68 C220 70 440 48 664 10 L664 110 L0 110 Z" fill="#fff"/>
    <path d="M0 74 C220 76 440 54 664 16 L664 110 L0 110 Z" fill="var(--charcoal)"/>
  </svg>

  <footer class="contact">
    <span>
      <svg width="12" height="12" viewBox="0 0 12 12" aria-hidden="true"><circle cx="6" cy="6" r="5" fill="none" stroke="#fff" stroke-width="1.3"/><path d="M1 6h10M6 1c-2.5 3-2.5 7 0 10M6 1c2.5 3 2.5 7 0 10" fill="none" stroke="#fff" stroke-width="1"/></svg>
      www.torvelcleaning.example
    </span>
    <span>
      <svg width="10" height="13" viewBox="0 0 10 13" aria-hidden="true"><path d="M5 0C2.2 0 0 2.2 0 5c0 3.5 5 8 5 8s5-4.5 5-8C10 2.2 7.8 0 5 0Zm0 7a2 2 0 1 1 0-4 2 2 0 0 1 0 4Z" fill="#fff"/></svg>
      Al Noor Garden Street Doha Qatar
    </span>
  </footer>
</article>
</body>
</html>
```